Gourmet food company looking for a dazzling label for their premuim vinagrette dressings

Need a food label that will dazzle our customer and prove what a premium product we have. We make high end gourmet dressing for vegetables, fruit, meat, poultry and fish.

Our label will fit on a 250 mil Tolvenna Square bottle. Labels should be a 4x5 or even 5x5 depending on the design. Nutritionals, bar codes and company blurb will be supplied later. We really want to test you all's talent on this one and are very excited to see your renderings!

Our dressings are Champagne Pear Vinaigrette, White Balsmic Vinaigrette, Mojito Lime Vinaigrette, Creamy-Avacado Lime Vinaigrette, and Asian Sesame Vinaigrette. I hope these names will help you envision our product and kinda what we are looking for.

Thank you all so far for your renderings.I really don't want pictures if that helps. Our logo can be smaller and/or the name of the product bigger. Perhaps we can even redesign Lumora and remove the leaf as I don't really care for what I see yet.So good luck and thanks Added Friday, August 19, 2016

I am still looking for that clean - elegant design for our product as our product is just that. If you look on the internet at vinegars and oils you will see many designs that are simple yet elegant. Creative lettering, bordering, color (can be black and white) and size will help accomplish this. So I invite you to use all your creativity and help me find just what we need.Many thanks Added Tuesday, August 23, 2016

Project Deadline Extended Reason: So many great designs coming in that I wanted a few extra days to tweek!Great job all Added Friday, August 26, 2016

Project Deadline Extended Reason: Very good designs thus far. We just need a few more days.Thanks Added Wednesday, August 31, 2016

Target Market(s)

High end grocery and specialty stores.

Our side panel on the label will say "At Lumora we're fanatics for great flavors and are passionate about finding the best ingredients. From simple to elegant our products are "simply lumora".

Industry/Entity Type

It Company

Font styles to use
Serif
Decorative
Script

Requirements
Must have
• A label that will draw the consumer to pick it up! Need something bold and elegant...
Nice to have
• Again, I really would like to have a label that pops. Since the bottle front is only about 2inches in width it will need some creativity. Would like something very simple and elegant.
• If the designer does not like the logo, please feel free to design without it!
Should not have
• Dark dark colors. We are selling dressing and we don't want any colors that may distort the contents.
• No stock photos for the front. I don't want our dressing to look like the others on the self. Brackwell Pantry just uses lettering and a their packaging is eye catching

```html
<!DOCTYPE html>
<html lang="en">
<head>
<meta charset="utf-8">
<title>Lumora – Asian Sesame Vinaigrette Label</title>
<link href="https://fonts.googleapis.com/css2?family=Alegreya+Sans:wght@400;500&family=Cormorant+Garamond:ital,wght@1,400&family=Italianno&family=Metamorphous&display=swap" rel="stylesheet">
<style>
  :root {
    --ink: #111111;
    --text: #333333;
    --paper: #ffffff;
  }
  * { margin: 0; padding: 0; box-sizing: border-box; }
  html, body { width: 960px; height: 1200px; overflow: hidden; background: var(--paper); }
  .label { position: relative; width: 960px; height: 1200px; color: var(--text); font-family: "Alegreya Sans", sans-serif; }
  .label-frame { position: absolute; left: 0; top: 0; }
  .script { font-family: "Italianno", cursive; color: var(--text); font-weight: 400; }
  .block { position: absolute; text-align: center; }

  .section-title { font-size: 38px; line-height: 1; }
  .body-copy { font-size: 14px; line-height: 20px; }

  .ingredients { left: 26px; top: 248px; width: 200px; }
  .ingredients .section-title { margin-bottom: 4px; }

  .brand { left: 280px; top: 236px; width: 400px; }
  .brand-name { font-size: 80px; line-height: 1; color: var(--ink); }
  .brand-tagline { font-size: 32px; line-height: 1; margin-top: 2px; }

  .nutrition-title { left: 28px; top: 438px; width: 180px; }
  .nutrition-table { position: absolute; left: 48px; top: 486px; border-collapse: collapse; font-size: 14px; }
  .nutrition-table td { height: 28.6px; padding: 0; }
  .nutrition-table .nutrient { width: 84px; padding-right: 14px; border-right: 1.5px solid var(--ink); }
  .nutrition-table .amount { padding-left: 14px; }

  .plaque { position: absolute; left: 0; top: 0; }
  .product-name { position: absolute; left: 238px; top: 500px; width: 484px; text-align: center;
    font-family: "Metamorphous", serif; font-size: 40px; line-height: 59px; color: var(--ink); letter-spacing: 0.5px; }

  .instructions { left: 742px; top: 248px; width: 198px; }
  .instructions .section-title { margin-bottom: 4px; }
  .instructions .body-copy { font-size: 15px; }

  .company { left: 740px; top: 500px; width: 200px; font-style: normal; }
  .company-name { font-size: 30px; line-height: 1; }

  .contact { left: 740px; top: 714px; width: 200px; font-size: 11px; line-height: 18px; font-style: normal; }
  .storage { left: 730px; top: 776px; width: 220px; font-size: 22px; }

  .marks { position: absolute; left: 742px; top: 810px; }
  .code-panel { position: absolute; left: 741px; top: 861px; width: 189px; height: 89px; background: var(--ink); }

  .logo { position: absolute; left: 42px; top: 896px; }
  .logo-name { font-size: 36px; line-height: 1; color: var(--ink); font-weight: 400; letter-spacing: 0.5px; }
  .logo-tagline { font-size: 10px; line-height: 1; color: var(--text); }

  .volume { position: absolute; left: 380px; top: 944px; width: 200px; text-align: center;
    font-family: "Cormorant Garamond", serif; font-style: italic; font-size: 26px; color: var(--text); }
</style>
</head>
<body>
<main class="label">
  <svg class="label-frame" width="960" height="1200" viewBox="0 0 960 1200" aria-hidden="true">
    <path d="M4,187 H350 C380,135 430,125 480,125 C530,125 580,135 610,187 H956 V1021 H610 C580,1073 530,1083 480,1083 C430,1083 380,1073 350,1021 H4 Z"
          fill="none" stroke="var(--ink)" stroke-width="6"/>
  </svg>

  <section class="block ingredients">
    <h2 class="script section-title">Ingredients</h2>
    <p class="body-copy">Ingredients goes here<br>Ingredients 02 goes here,<br>Ingredients 03 goes here,<br>Ingredients 04.</p>
  </section>

  <header class="block brand">
    <h1 class="script brand-name">Lumora</h1>
    <p class="script brand-tagline">Graceful Gourmet Dressings</p>
  </header>

  <h2 class="block script section-title nutrition-title">Nutritionals</h2>
  <table class="nutrition-table">
    <tr><td class="nutrient">Nutritionals</td><td class="amount">OO oz</td></tr>
    <tr><td class="nutrient">Nutritionals</td><td class="amount">OO oz</td></tr>
    <tr><td class="nutrient">Nutritionals</td><td class="amount">OO oz</td></tr>
    <tr><td class="nutrient">Nutritionals</td><td class="amount">OO oz</td></tr>
    <tr><td class="nutrient">Nutritionals</td><td class="amount">OO oz</td></tr>
    <tr><td class="nutrient">Nutritionals</td><td class="amount">OO oz</td></tr>
  </table>

  <svg class="plaque" width="960" height="1200" viewBox="0 0 960 1200" aria-hidden="true">
    <defs>
      <path id="plaque-shape" d="M276,500 H350 C362,470 420,454 480,454 C540,454 598,470 610,500 H684 V530 C710,540 722,570 722,600 C722,630 710,660 684,670 V698 H610 C598,728 540,746 480,746 C420,746 362,728 350,698 H276 V670 C250,660 238,630 238,600 C238,570 250,540 276,530 Z"/>
    </defs>
    <use href="#plaque-shape" fill="var(--ink)"/>
    <use href="#plaque-shape" fill="var(--paper)" transform="translate(480 600) scale(0.965 0.945) translate(-480 -600)"/>
    <use href="#plaque-shape" fill="none" stroke="var(--ink)" stroke-width="2" stroke-dasharray="0.1 8" stroke-linecap="round"
         transform="translate(480 600) scale(0.93 0.895) translate(-480 -600)"/>
  </svg>
  <h2 class="product-name">ASIAN<br>SESAME<br>VINAIGRETTE</h2>

  <section class="block instructions">
    <h2 class="script section-title">Instructions</h2>
    <p class="body-copy">Lorem Ipsum is simply dummy text of the printing and typesetting industry. Lorem Ipsum has been the industry's standard dummy text ever since the 1500s, when an unknown printer took a galley of type and scrambled it to make a type specimen book.</p>
  </section>

  <address class="block company">
    <p class="script company-name">Lumora Dressing Ltd.</p>
    <p class="body-copy">412 Harlow Lane, 2nd Floor |<br>Fairbrook, OR 97000</p>
  </address>

  <address class="block contact">
    www.lumoradressing.com<br>hello@lumoradressing.com<br>(000) 000 000
  </address>

  <p class="block script storage">Store in a cold and dark place</p>

  <svg class="marks" width="190" height="50" viewBox="0 0 190 50" aria-hidden="true">
    <circle cx="22" cy="22" r="17" fill="none" stroke="var(--ink)" stroke-width="5" stroke-dasharray="22 5"/>
    <circle cx="70" cy="18" r="14" fill="var(--paper)" stroke="var(--ink)" stroke-width="2"/>
    <rect x="63" y="30" width="14" height="14" fill="var(--ink)"/>
    <circle cx="118" cy="22" r="18" fill="var(--ink)"/>
    <circle cx="118" cy="22" r="13" fill="none" stroke="var(--paper)" stroke-width="1.5"/>
    <path d="M168,44 C154,42 152,28 160,20 C160,28 164,28 164,24 C164,14 170,8 170,2 C178,10 184,20 182,32 C181,40 176,44 168,44 Z" fill="var(--ink)"/>
  </svg>
  <div class="code-panel"></div>

  <div class="logo">
    <p class="logo-name">Lumora</p>
    <p class="logo-tagline">Graceful Gourmet Dressings</p>
  </div>

  <p class="volume">250 ml</p>
</main>
</body>
</html>
```